Criação de Papelaria para Arquitetura
A empresa queria:
" Escritório fundado por dois sócios ( Bordalo & Quintela ) com atuação desde a criação do projeto arquitetônico, compatibilização de projetos complementares e a construção - gerenciamento de obras. Maiores informações: www.bqarquitetos-exemplo.com.br "

```html
<!DOCTYPE html>
<html lang="pt-BR">
<head>
<meta charset="utf-8">
<title>Bordalo &amp; Quintela — Papelaria</title>
<link rel="stylesheet" href="https://fonts.googleapis.com/css2?family=Raleway:wght@300;400&display=swap">
<style>
  :root {
    --backdrop: #e4e4e4;
    --envelope-dark: #0d0d0d;
    --flap-dark: #4b4b4b;
    --flap-edge: #6a6a6a;
    --envelope-light: #ffffff;
    --ink-dark: #2a2a2a;
    --ink-light: #f2f2f2;
    --ink-muted: #9a9a9a;
  }
  * { box-sizing: border-box; margin: 0; padding: 0; }
  html, body {
    width: 1200px; height: 1200px; overflow: hidden;
    background: var(--backdrop);
    font-family: "Raleway", sans-serif;
  }
  .stationery {
    position: relative; width: 1200px; height: 1200px;
  }
  .envelope {
    position: absolute; left: 150px; width: 900px; height: 420px;
    box-shadow: 0 6px 18px rgba(0,0,0,0.18);
  }
  .envelope--back { top: 140px; background: var(--envelope-dark); }
  .envelope--front { top: 640px; background: var(--envelope-light); }

  .envelope__flap {
    position: absolute; inset: 0; width: 900px; height: 420px;
  }

  .contact-list {
    position: absolute; left: 48px; top: 46px;
    list-style: none; display: flex; flex-direction: column; gap: 9px;
  }
  .contact-list__item {
    display: flex; align-items: center; gap: 10px;
    color: var(--ink-muted); font-size: 11px; font-weight: 400; letter-spacing: 0.3px;
  }
  .contact-list__icon { width: 14px; height: 14px; flex: none; }

  .brand-name {
    position: absolute; font-weight: 300; white-space: nowrap; letter-spacing: 0.5px;
  }
  .envelope--back .brand-name {
    right: 200px; bottom: 58px; font-size: 30px; color: var(--ink-light);
  }
  .envelope--front .brand-name {
    left: 250px; top: 178px; font-size: 40px; color: var(--ink-dark);
  }
</style>
</head>
<body>
<main class="stationery">

  <section class="envelope envelope--back" aria-label="Verso do envelope">
    <svg class="envelope__flap" viewBox="0 0 900 420" aria-hidden="true">
      <polygon points="900,0 700,0 790,190 800,230 900,420" fill="var(--flap-dark)"/>
      <polyline points="700,0 790,190 800,230 900,420" fill="none" stroke="var(--flap-edge)" stroke-width="2"/>
    </svg>

    <ul class="contact-list">
      <li class="contact-list__item">
        <svg class="contact-list__icon" viewBox="0 0 14 14" aria-hidden="true">
          <rect x="0.5" y="0.5" width="13" height="13" fill="none" stroke="var(--ink-muted)"/>
          <path d="M4 3.5h2l.6 2-1 .8a5 5 0 0 0 2.1 2.1l.8-1 2 .6v2a1 1 0 0 1-1 1A6.5 6.5 0 0 1 3 4.5a1 1 0 0 1 1-1z" fill="var(--ink-muted)"/>
        </svg>
        (11) 3456-7890
      </li>
      <li class="contact-list__item">
        <svg class="contact-list__icon" viewBox="0 0 14 14" aria-hidden="true">
          <rect x="0.5" y="0.5" width="13" height="13" fill="none" stroke="var(--ink-muted)"/>
          <rect x="3" y="4" width="8" height="6" fill="none" stroke="var(--ink-muted)"/>
          <path d="M3 4l4 3.2L11 4" fill="none" stroke="var(--ink-muted)"/>
        </svg>
        contato@bqarquitetos-exemplo.com.br
      </li>
      <li class="contact-list__item">
        <svg class="contact-list__icon" viewBox="0 0 14 14" aria-hidden="true">
          <rect x="0.5" y="0.5" width="13" height="13" fill="none" stroke="var(--ink-muted)"/>
          <circle cx="7" cy="7" r="3.6" fill="none" stroke="var(--ink-muted)"/>
          <path d="M3.4 7h7.2M7 3.4c-1.6 2-1.6 5.2 0 7.2M7 3.4c1.6 2 1.6 5.2 0 7.2" fill="none" stroke="var(--ink-muted)" stroke-width="0.8"/>
        </svg>
        www.bqarquitetos-exemplo.com.br
      </li>
      <li class="contact-list__item">
        <svg class="contact-list__icon" viewBox="0 0 14 14" aria-hidden="true">
          <rect x="0.5" y="0.5" width="13" height="13" fill="none" stroke="var(--ink-muted)"/>
          <path d="M7 11.2S4 8.2 4 6a3 3 0 0 1 6 0c0 2.2-3 5.2-3 5.2z" fill="var(--ink-muted)"/>
          <circle cx="7" cy="6" r="1" fill="var(--envelope-dark)"/>
        </svg>
        Rua das Palmeiras, 120 · São Paulo SP
      </li>
    </ul>

    <p class="brand-name">Bordalo &amp; Quintela</p>
  </section>

  <section class="envelope envelope--front" aria-label="Frente do envelope">
    <p class="brand-name">Bordalo &amp; Quintela</p>
  </section>

</main>
</body>
</html>
```